Chiropractic office needs updated web site

take the information/content from my existing website and redesign it to be more efficient and modern looking. i have a logo already designed that i have provided the files for. my office sees primarily athletes and their families and is geared toward active, healthy people who have sports injuries.
Updates

i originally started the project in february 2019 but am now just able to post the project. i need a new deadline calculated from todays (6-9-19) date.

Designs look the same

Target Market(s)

injured athletes looking for a specific type of chiropractor.

Industry/Entity Type

Health Care

Contact Information for Business Card

I have a logo already designed and will provide that to all designers!

Coding

Coded - Design and coding required

Number of Pages Required

1 page

Font styles to use
Sans Serif

Colors

Designer to choose colors to be used in the design.

Requirements
Must have
• the current information/content already contained in my current website, dellwynspinefit.com. i want this info redesigned and/or transferred to a new template. i will also provide new updated photos for use on the new site!
Nice to have
• modern, minimalist, creative looking website
Should not have
• typical medical website with boring, over-used stock photos of doctors, nurses and generic family types

```html
<!DOCTYPE html>
<html lang="en">
<head>
<meta charset="utf-8">
<title>Dellwyn Chiropractic and Sports Therapy</title>
<link href="https://fonts.googleapis.com/css2?family=Orbitron:wght@600;700&family=Montserrat:wght@400;500;600&display=swap" rel="stylesheet">
<style>
:root{
  --sky:#d3eefa;
  --pale:#f1f8fc;
  --brand:#25aae8;
  --ink:#2b2b2b;
  --text:#3c3c3c;
  --rule:#e9a3ab;
  --link:#d8474f;
  --footer:#050505;
  --white:#ffffff;
}
*{margin:0;padding:0;box-sizing:border-box}
html,body{width:1200px;height:4892px;overflow:hidden;background:var(--white)}
body{font-family:"Montserrat",sans-serif;color:var(--text)}
.page{position:relative;width:1200px;height:4892px;overflow:hidden}
.abs{position:absolute}
.hero{left:0;top:0;width:1200px;height:507px;background:var(--sky)}
.brand{left:34px;top:26px;display:flex;align-items:center;gap:10px}
.brand-dot{width:42px;height:42px;border-radius:50%;background:var(--brand)}
.brand-name{font-family:"Montserrat",sans-serif;font-weight:600;font-size:17px;color:var(--brand);line-height:1.15;letter-spacing:.5px}
.menu{left:1143px;top:30px}
.headline{left:0;top:200px;width:1200px;text-align:center;font-family:"Orbitron",sans-serif;font-weight:700;font-size:66px;color:var(--brand);letter-spacing:2px;word-spacing:40px}
.tagline{left:0;top:318px;width:1200px;text-align:center;font-size:27px;color:var(--ink);letter-spacing:.5px}
.intro{left:250px;top:600px;width:700px;text-align:center;font-size:21.5px;line-height:33px;color:var(--text)}
.block{background:var(--pale)}
.photo{}
.title{font-size:25px;font-weight:500;color:var(--ink);letter-spacing:.5px}
.rule{height:1px;background:var(--rule)}
.copy{width:385px;font-size:14.6px;line-height:26.8px;color:var(--text)}
.copy p+p{margin-top:26px}
.more{font-size:13.5px;color:var(--link);text-decoration:underline}
.sub{left:0;width:1200px;text-align:center;font-size:25px;color:var(--ink);letter-spacing:.5px}
.footer{left:0;top:4558px;width:1200px;height:334px;background:var(--footer);color:var(--white)}
.ft{font-size:13px;color:var(--white)}
.follow{font-weight:600;font-size:15px;letter-spacing:1px}
.social{display:flex;gap:6px}
.social span{width:25px;height:25px;border-radius:50%;background:var(--white)}
</style>
</head>
<body>
<div class="page">
  <header class="abs hero"></header>
  <div class="abs brand"><span class="brand-dot"></span><span class="brand-name">DELLWYN<br>CHIROPRACTIC &amp; SPORTS</span></div>
  <svg class="abs menu" width="24" height="18" viewBox="0 0 24 18"><rect y="0" width="24" height="2" fill="#222"/><rect y="8" width="24" height="2" fill="#222"/><rect y="16" width="24" height="2" fill="#222"/></svg>
  <h1 class="abs headline">MUSCLE. JOINT. NERVE.</h1>
  <p class="abs tagline">TAKE CONTROL OF YOUR HEALTH AND WELL-BEING.</p>
  <p class="abs intro">The Dellwyn Protocol is profoundly effective in the treatment of athletic injuries, chronic pain and stiffness and many of the functional difficulties normally associated with aging.</p>

  <!-- Protocol -->
  <div class="abs block" style="left:0;top:778px;width:640px;height:324px"></div>
  <div class="abs photo" role="img" aria-label="Beach volleyball players leaping at the net" style="left:173px;top:879px;width:406px;height:561px;background:linear-gradient(160deg,#c9a63a,#3b5fa8 55%,#d8c046)"></div>
  <h2 class="abs title" style="left:670px;top:910px">The Dellwyn Protocol</h2>
  <div class="abs rule" style="left:619px;top:948px;width:543px"></div>
  <div class="abs copy" style="left:670px;top:964px">
    <p>The Dellwyn Protocol, or TDP, is a comprehensive system of chiropractic and soft tissue therapy developed to diagnose and treat neuromusculo-skeletal (nerve, muscle, bone) injury and dysfunction. Conditions such as joint and muscle pain, spasm, headache, numbness, weakness, excessive tension and reduced range of motion typically respond extremely well to TDP.</p>
    <p>Although the majority of the work is applied manually by the Doctor or trained practitioner, some use of therapeutic tools is relied upon.</p>
  </div>
  <a class="abs more" style="left:671px;top:1301px">Read More</a>

  <!-- Myofascial -->
  <div class="abs block" style="left:535px;top:1540px;width:665px;height:325px"></div>
  <div class="abs photo" role="img" aria-label="Climber scaling a dark rock face" style="left:596px;top:1643px;width:407px;height:560px;background:linear-gradient(160deg,#3e4a48,#2a6b6c 50%,#1e2322)"></div>
  <h2 class="abs title" style="left:121px;top:1673px">Myofascial Therapy</h2>
  <div class="abs rule" style="left:93px;top:1713px;width:463px"></div>
  <div class="abs copy" style="left:121px;top:1728px">
    <p>Myofascial therapy is a safe, low force therapy that releases and heals soft tissue restrictions and tightness that cause pain throughout the body. The myofascial system consists of fascia, a three-dimensional connective tissue web that spreads throughout the body surrounding every muscle, bone, nerve, blood vessel and organ.</p>
    <p>When fascia is in its normal healthy state it is a relaxed connective tissue web, but when this fascia is tight and restricted the web is more rigid and pliable.</p>
  </div>
  <a class="abs more" style="left:121px;top:2065px">Read More</a>

  <!-- ART -->
  <div class="abs block" style="left:0;top:2303px;width:640px;height:323px"></div>
  <div class="abs photo" role="img" aria-label="Two lacrosse players colliding mid-game" style="left:173px;top:2406px;width:406px;height:558px;background:linear-gradient(160deg,#8b7a5e,#2e3448 50%,#b9ab8f)"></div>
  <h2 class="abs title" style="left:670px;top:2435px">Active Release Therapy</h2>
  <div class="abs rule" style="left:619px;top:2473px;width:543px"></div>
  <div class="abs copy" style="left:670px;top:2491px">
    <p>Active Release Therapy (ART) is extremely effective in soft tissue treatment. ART is a massage-based technique that targets a range of problems related to muscles, tendons, ligaments, fascia and nerves. Conditions related to the build up of adhesions and scar tissue in muscle result in several problems to the muscle.</p>
    <p>Muscles become shorter &amp;amp; weaker, joints are altered and nerves become compressed. As a result, the affected muscles suffer from pain, decreased bloodsupply and poor mobility.</p>
  </div>
  <a class="abs more" style="left:670px;top:2828px">Read More</a>

  <!-- Trigger point -->
  <div class="abs block" style="left:535px;top:3065px;width:665px;height:325px"></div>
  <div class="abs photo" role="img" aria-label="Football resting on a dusty field line" style="left:596px;top:3167px;width:407px;height:559px;background:linear-gradient(170deg,#c4a98a,#a9835e 60%,#8b5a36)"></div>
  <h2 class="abs title" style="left:121px;top:3197px">Trigger Point</h2>
  <div class="abs rule" style="left:93px;top:3238px;width:463px"></div>
  <div class="abs copy" style="left:121px;top:3252px">
    <p>Trigger point therapy addresses most muscle pains, which can occur at various points in the body called trigger points. This type of therapy focuses under the principle that tight muscles form bands or knots where waste products from the body can accumulate. These hyperirritable painful spots put pressure on the surrounding nerve clusters when they are activated, but can be painful to the touch even when they are latent or inactive.</p>
    <p>The formation is called a trigger point andstress on the muscle can cause the trigger point to activate causing a sharp pain.</p>
  </div>
  <a class="abs more" style="left:121px;top:3645px">Read More</a>

  <!-- Testimonials -->
  <h2 class="abs sub" style="top:3846px">Words that Say a Lot!</h2>
  <div class="abs" role="img" aria-label="Volleyball player diving with handwritten thank-you note" style="left:63px;top:3912px;width:250px;height:199px;background:linear-gradient(160deg,#7aa8d8,#e8b27a)"></div>
  <div class="abs" role="img" aria-label="Volleyball players at the net with handwritten note" style="left:325px;top:3912px;width:254px;height:199px;background:linear-gradient(160deg,#5b8fc4,#d9c7b0)"></div>
  <div class="abs" role="img" aria-label="Indoor volleyball spike with handwritten note" style="left:589px;top:3912px;width:277px;height:199px;background:linear-gradient(160deg,#e8e2dc,#6b2b30)"></div>
  <div class="abs" role="img" aria-label="Beach volleyball block with handwritten note" style="left:877px;top:3912px;width:253px;height:199px;background:linear-gradient(160deg,#27b6e6,#d4c8a8)"></div>
  <a class="abs more" style="left:562px;top:4140px">Read More</a>

  <!-- Stay fit -->
  <h2 class="abs sub" style="top:4247px">#StayFit-Healthy</h2>
  <div class="abs" role="img" aria-label="Team of athletes seated together in the clinic" style="left:63px;top:4312px;width:250px;height:200px;background:linear-gradient(160deg,#8d8f96,#c7a88c)"></div>
  <div class="abs" role="img" aria-label="Athletes posing with a patient outdoors" style="left:325px;top:4312px;width:254px;height:200px;background:linear-gradient(160deg,#d8d4cc,#6d88b0)"></div>
  <div class="abs" role="img" aria-label="Musician performing on a blue-lit stage" style="left:589px;top:4312px;width:277px;height:200px;background:linear-gradient(160deg,#1c2f8c,#3b78d8)"></div>
  <div class="abs" role="img" aria-label="Patient and doctor smiling in the office" style="left:877px;top:4312px;width:253px;height:200px;background:linear-gradient(160deg,#efeae4,#2c6fa8)"></div>

  <!-- Footer -->
  <footer class="abs footer">
    <div class="abs" role="img" aria-label="Athlete's muscular back in low light" style="left:325px;top:0;width:875px;height:334px;background:radial-gradient(ellipse 180px 260px at 720px 150px,#4a3a30,rgba(5,5,5,0) 100%)"></div>
    <p class="abs ft follow" style="left:139px;top:62px">FOLLOW US</p>
    <div class="abs social" style="left:139px;top:96px"><span></span><span></span><span></span><span></span></div>
    <p class="abs ft" style="left:135px;top:158px;line-height:19px">418 Meridian Way<br>Fairbrook, TX 75190</p>
    <p class="abs ft" style="left:135px;top:216px">555.014.2290</p>
    <p class="abs ft" style="left:454px;top:64px;line-height:25px">Terms &amp; Conditions<br>Privacy Policy</p>
    <p class="abs ft" style="left:0;width:1200px;text-align:center;top:296px;font-size:12px">© 2019 Dellwyn Chiropractic and Sports Therapy.</p>
  </footer>
</div>
</body>
</html>
```